Lantern and Tides Garden of Seasons - A user friendly psychology model

Thank you for looking at my psychology business project.
- I am currently running 3 design contests (2 x logos + 1 x infographic/graphic design)
- Please look at all 3 currently listed projects
- I have several other infographic/poster projects to complete this month, and will post these jobs after the first 3 contests are complete

This graphic design/infographic contest is to draw a client-friendly version of a theoretical model of positive psychology. This resource will be used by therapists with clients. I have provided a draft copy of the design along with a copy of the academic version of the model, which this graphic is based on. Ideally, we want the message of the model to be communicated in images as much as possible. I am very open to your creative input in this project.

The full project will have around 10 different design components. I expect to have a further 7 graphic illustrations drawn and the winner of this contest will be my first point of contact to for the other pieces of work. Of the whole project, this piece of work is the most important to me, and I am very grateful for your creative contributions.

A note more broadly on the full project:
The purpose of the project is to promote a new theory of psychology which I have developed, called “Adaptive-Harmonic Theory”. This theory is not yet in the public domain, and I will be introducing it at a psychology conference in July this year.
The theory suggests that the intersection of experiences and relationships is a fundamental determinant of psychological growth and regression across the life span. It emphasises the importance of healthy connected relationships and having enjoyable and fun experiences. In a nutshell, it says that we thrive when we share positive experiences with other people, and we suffer when we have poor relationships and negative experiences. The model emphasises the interplay of 5 key factors: relationships, experiences, mental state, embodiment, and growth.

Thanks so much for your time looking at my project. I very much appreciate your efforts. 😊
Kind regards, Tav.

Target Market(s)

People interested in personal development

Industry/Entity Type

Psychology, self improvement, personal development, coaching

Font styles to use
Other font styles liked:
• Please choose fonts as you see fit

Requirements
Must have
• Must be based on the mock-up provided. Please use the same text as used on the draft. Please use the similar colour squares for each section of the model as shown in the accademic version of the model. The end product will primarily be used as an A4 handout, however, I also need to be able to print it at poster size for conference presentations.
Nice to have
• colourful, images to tell the story of the model, easy to read, user friendly
Should not have
• I am open to your creative input

```html
<!DOCTYPE html>
<html lang="en">
<head>
<meta charset="utf-8">
<title>Lantern and Tides Garden of Seasons</title>
<link rel="stylesheet" href="https://fonts.googleapis.com/css2?family=Saira+Semi+Condensed:wght@500;600&family=Roboto+Slab:wght@600;700&family=Inter:wght@400;600&display=swap">
<style>
  :root{
    --navy:#20283a;
    --space:#1e2537;
    --cream:#ece7dc;
    --divider:#b9b6ae;
    --ring:#a7a6a4;
    --gold:#f2a93b;
    --orange:#f2a53a;
    --red:#e2493a;
    --crimson:#d63545;
    --green:#3c8e5a;
    --teal:#3aa2c4;
    --blue:#2d5ea8;
    --purple:#6a3a8c;
    --violet:#7a5aa8;
    --ink:#2b2b35;
    --muted:#6d6c72;
    --white:#ffffff;
    --frame:#8b93a6;
  }
  html,body{margin:0;padding:0;overflow:hidden}
  body{width:1200px;height:892px;background:var(--navy);position:relative;font-family:"Inter",sans-serif}
  .poster{position:absolute;left:310px;top:159px;width:580px;height:575px}
  .poster svg{position:absolute;left:0;top:0;width:580px;height:575px}
  .title{position:absolute;font-family:"Saira Semi Condensed",sans-serif;font-weight:500;font-size:17.5px;line-height:18px;letter-spacing:.3px;text-transform:uppercase;margin:0}
  .title-left{left:12px;top:18px;color:var(--gold)}
  .title-right{right:16px;top:18px;text-align:right;color:var(--white)}
  .title-right .accent{color:var(--gold);font-weight:600}
  .lobe-head{font-family:"Roboto Slab",serif;font-weight:700;font-size:5.6px;fill:var(--ink)}
  .lobe-sub{font-family:"Inter",sans-serif;font-weight:600;font-size:3.9px;fill:var(--ink)}
  .lobe-body{font-family:"Inter",sans-serif;font-size:3.6px;fill:var(--muted)}
  .node-head{font-family:"Roboto Slab",serif;font-weight:700;font-size:4.4px;fill:var(--white)}
  .node-body{font-family:"Inter",sans-serif;font-size:3.5px;fill:var(--ink)}
  .hub-text{font-family:"Roboto Slab",serif;font-weight:700;font-size:4.3px;fill:#fbe1c2}
  .note{font-family:"Inter",sans-serif;font-size:3.6px;fill:#a9aec0}
</style>
</head>
<body>
<main class="poster">
  <svg viewBox="0 0 580 575" xmlns="http://www.w3.org/2000/svg">
    <rect class="frame" x="6" y="6" width="568" height="563" fill="none" stroke="var(--frame)" stroke-width=".8"/>
    <ellipse cx="290" cy="290" rx="262" ry="262" fill="none" stroke="#5b6b8a" stroke-width=".8" stroke-dasharray="2 3"/>
    <g class="orbit-dots">
      <circle cx="388" cy="18" r="5" fill="var(--gold)"/>
      <circle cx="565" cy="172" r="6" fill="var(--teal)"/>
      <circle cx="558" cy="207" r="5" fill="var(--gold)"/>
      <circle cx="558" cy="400" r="5" fill="var(--gold)"/>
      <circle cx="553" cy="433" r="6" fill="var(--green)"/>
      <circle cx="410" cy="548" r="6" fill="var(--gold)"/>
      <circle cx="372" cy="558" r="6" fill="var(--teal)"/>
      <circle cx="153" cy="540" r="6" fill="var(--gold)"/>
      <circle cx="17" cy="378" r="5" fill="var(--gold)"/>
      <circle cx="25" cy="176" r="12" fill="var(--teal)"/>
      <circle cx="24" cy="96" r="5" fill="var(--gold)"/>
    </g>

    <g role="img" aria-label="Heart-shaped balloon floating in the night sky"><ellipse cx="182" cy="22" rx="9" ry="8" fill="#4fb3d6"/></g>
    <g role="img" aria-label="Green heart illustration"><ellipse cx="31" cy="119" rx="17" ry="13" fill="var(--green)"/></g>
    <g role="img" aria-label="Blue heart with a speech bubble in a circle"><circle cx="550" cy="117" r="19" fill="var(--gold)"/></g>
    <g role="img" aria-label="Blue flower holding a small lightbulb"><circle cx="51" cy="268" r="21" fill="var(--blue)"/></g>
    <g role="img" aria-label="Yellow flower with a compass in the centre"><circle cx="36" cy="446" r="23" fill="var(--gold)"/></g>
    <g role="img" aria-label="Landscape of blue waves and red hills"><rect x="476" y="466" width="74" height="60" rx="6" fill="#4a90b8"/></g>

    <g class="lobes" fill="var(--cream)">
      <circle cx="290" cy="281" r="205"/>
      <circle cx="495" cy="281" r="58"/><circle cx="478" cy="178" r="62"/>
      <circle cx="393" cy="103" r="62"/><circle cx="290" cy="80" r="62"/>
      <circle cx="187" cy="103" r="62"/><circle cx="102" cy="178" r="62"/>
      <circle cx="85" cy="281" r="58"/><circle cx="102" cy="384" r="62"/>
      <circle cx="187" cy="459" r="62"/><circle cx="290" cy="482" r="62"/>
      <circle cx="393" cy="459" r="62"/><circle cx="478" cy="384" r="62"/>
    </g>
    <g class="dividers" stroke="var(--divider)" stroke-width="4" stroke-linecap="round">
      <line x1="217" y1="155" x2="165" y2="66"/><line x1="363" y1="155" x2="415" y2="66"/>
      <line x1="416" y1="208" x2="505" y2="156"/><line x1="416" y1="354" x2="505" y2="406"/>
      <line x1="363" y1="407" x2="415" y2="496"/><line x1="217" y1="407" x2="165" y2="496"/>
      <line x1="164" y1="354" x2="75" y2="406"/><line x1="164" y1="208" x2="75" y2="156"/>
      <line x1="132" y1="281" x2="62" y2="281"/><line x1="448" y1="281" x2="500" y2="281"/>
      <line x1="290" y1="123" x2="290" y2="75"/><line x1="290" y1="439" x2="290" y2="478"/>
    </g>

    <g class="band" fill="none" stroke-width="46">
      <circle cx="290" cy="281" r="127" stroke="var(--green)" stroke-dasharray="79.8 800" transform="rotate(-126 290 281)"/>
      <circle cx="290" cy="281" r="127" stroke="var(--teal)" stroke-dasharray="79.8 800" transform="rotate(-90 290 281)"/>
      <circle cx="290" cy="281" r="127" stroke="var(--gold)" stroke-dasharray="79.8 800" transform="rotate(-54 290 281)"/>
      <circle cx="290" cy="281" r="127" stroke="#ec7a34" stroke-dasharray="79.8 800" transform="rotate(-18 290 281)"/>
      <circle cx="290" cy="281" r="127" stroke="var(--crimson)" stroke-dasharray="79.8 800" transform="rotate(18 290 281)"/>
      <circle cx="290" cy="281" r="127" stroke="var(--purple)" stroke-dasharray="79.8 800" transform="rotate(54 290 281)"/>
      <circle cx="290" cy="281" r="127" stroke="var(--red)" stroke-dasharray="79.8 800" transform="rotate(90 290 281)"/>
      <circle cx="290" cy="281" r="127" stroke="var(--purple)" stroke-dasharray="79.8 800" transform="rotate(126 290 281)"/>
      <circle cx="290" cy="281" r="127" stroke="var(--teal)" stroke-dasharray="79.8 800" transform="rotate(162 290 281)"/>
      <circle cx="290" cy="281" r="127" stroke="var(--green)" stroke-dasharray="79.8 800" transform="rotate(198 290 281)"/>
    </g>
    <circle cx="290" cy="281" r="104" fill="none" stroke="var(--blue)" stroke-width="5"/>
    <circle cx="290" cy="281" r="155" fill="none" stroke="var(--ring)" stroke-width="9"/>

    <circle cx="290" cy="281" r="101" fill="var(--space)"/>
    <g class="stars" fill="#ffffff">
      <circle cx="246" cy="213" r="1.3"/><circle cx="266" cy="230" r="1"/><circle cx="330" cy="216" r="1.2"/>
      <circle cx="358" cy="246" r="1"/><circle cx="228" cy="262" r="1.2"/><circle cx="214" cy="300" r="1"/>
      <circle cx="252" cy="338" r="1.3"/><circle cx="330" cy="340" r="1"/><circle cx="362" cy="318" r="1.2"/>
      <circle cx="300" cy="362" r="1"/><circle cx="270" cy="196" r="1"/><circle cx="350" cy="290" r="1"/>
    </g>
    <g class="planets">
      <circle cx="227" cy="322" r="3.5" fill="var(--gold)"/><circle cx="236" cy="352" r="4" fill="var(--teal)"/>
      <circle cx="264" cy="374" r="3.5" fill="var(--green)"/><circle cx="320" cy="374" r="3.5" fill="var(--gold)"/>
      <circle cx="348" cy="358" r="3.5" fill="var(--teal)"/><circle cx="342" cy="246" r="3.5" fill="var(--gold)"/>
      <circle cx="346" cy="270" r="3.5" fill="var(--green)"/>
    </g>
    <g class="spokes" stroke="var(--orange)" stroke-width="7" stroke-linecap="round">
      <line x1="290" y1="281" x2="290" y2="170"/><line x1="290" y1="281" x2="290" y2="392"/>
      <line x1="290" y1="281" x2="176" y2="281"/><line x1="290" y1="281" x2="404" y2="281"/>
      <line x1="290" y1="281" x2="222" y2="213"/><line x1="290" y1="281" x2="358" y2="213"/>
      <line x1="290" y1="281" x2="222" y2="349"/><line x1="290" y1="281" x2="358" y2="349"/>
    </g>
    <circle cx="290" cy="281" r="37" fill="var(--orange)"/>
    <circle cx="290" cy="281" r="31" fill="var(--red)"/>
    <circle cx="290" cy="281" r="24" fill="none" stroke="#f6b07a" stroke-width=".8"/>
    <text class="hub-text" text-anchor="middle"><tspan x="290" y="277">Adaptive-Harmonic</tspan><tspan x="290" dy="6">Theory</tspan><tspan x="290" dy="6">of Growth</tspan></text>

    <line x1="290" y1="75" x2="290" y2="105" stroke="var(--divider)" stroke-width="3"/>
    <line x1="290" y1="455" x2="290" y2="480" stroke="var(--divider)" stroke-width="3"/>

    <circle cx="290" cy="43" r="37" fill="var(--cream)" stroke="#c9c5bc" stroke-width="2"/>
    <g role="img" aria-label="Lightbulb with a growing tree inside"><circle cx="290" cy="43" r="31" fill="#5d55a3"/></g>
    <circle cx="290" cy="516" r="38" fill="var(--cream)" stroke="#c9c5bc" stroke-width="2"/>
    <g role="img" aria-label="Figure with outstretched arms balancing"><circle cx="290" cy="512" r="29" fill="none" stroke="var(--gold)" stroke-width="5"/></g>

    <g class="node">
      <circle cx="290" cy="142" r="28" fill="var(--white)" stroke="var(--red)" stroke-width="4"/>
      <rect x="274" y="127" width="32" height="8" rx="4" fill="var(--red)"/>
      <text class="node-head" x="290" y="133" text-anchor="middle">Relate</text>
      <text class="node-body" text-anchor="middle"><tspan x="290" y="145">Close bonds</tspan><tspan x="290" dy="5">with others</tspan></text>
    </g>
    <g class="node">
      <circle cx="197" cy="188" r="24" fill="var(--white)" stroke="var(--green)" stroke-width="4"/>
      <text class="node-head" x="197" y="181" text-anchor="middle" style="fill:var(--green)">Mind</text>
      <text class="node-body" x="197" y="191" text-anchor="middle">Inner calm</text>
    </g>
    <g class="node">
      <circle cx="138" cy="281" r="24" fill="var(--white)" stroke="var(--teal)" stroke-width="4"/>
      <text class="node-head" x="138" y="274" text-anchor="middle" style="fill:var(--teal)">Growth</text>
      <text class="node-body" text-anchor="middle"><tspan x="138" y="283">Learn and</tspan><tspan x="138" dy="5">stretch</tspan></text>
    </g>
    <g class="node">
      <circle cx="208" cy="389" r="25" fill="var(--white)" stroke="var(--blue)" stroke-width="4"/>
      <text class="node-head" x="208" y="382" text-anchor="middle" style="fill:var(--blue)">Body</text>
      <text class="node-body" x="208" y="392" text-anchor="middle">Move and rest</text>
    </g>
    <g class="node">
      <circle cx="291" cy="430" r="30" fill="var(--white)" stroke="var(--cream)" stroke-width="3"/>
      <path d="M263 423 Q263 410 276 410 L306 410 Q319 410 319 423 L319 428 L263 428 Z" fill="var(--violet)"/>
      <text class="node-head" x="291" y="418" text-anchor="middle">Experience</text>
      <text class="node-body" x="291" y="424.5" text-anchor="middle" style="fill:#f1ebfa">Fun shared</text>
      <text class="node-body" text-anchor="middle"><tspan x="291" y="437">Enjoy new</tspan><tspan x="291" dy="5">moments</tspan></text>
    </g>
    <g class="node">
      <circle cx="372" cy="389" r="25" fill="var(--white)" stroke="var(--purple)" stroke-width="4"/>
      <text class="node-head" x="372" y="382" text-anchor="middle" style="fill:var(--purple)">Balance</text>
      <text class="node-body" x="372" y="392" text-anchor="middle">Steady mood</text>
    </g>
    <g class="node">
      <circle cx="443" cy="281" r="25" fill="var(--white)" stroke="var(--crimson)" stroke-width="4"/>
      <text class="node-head" x="443" y="274" text-anchor="middle" style="fill:var(--crimson)">Thrive</text>
      <text class="node-body" text-anchor="middle"><tspan x="443" y="283">Together</tspan><tspan x="443" dy="5">we grow</tspan></text>
    </g>
    <g role="img" aria-label="Round emblem of a heart linked to a smaller circle">
      <circle cx="384" cy="189" r="24" fill="#58b4d4" stroke="#d9eef5" stroke-width="2"/>
    </g>

    <text class="lobe-head" x="189" y="69">Shared Moments</text>
    <text class="lobe-sub" x="189" y="75">Time well spent together</text>
    <text class="lobe-body"><tspan x="189" y="82">Warm time together builds</tspan><tspan x="189" dy="5">trust and a sense of</tspan><tspan x="189" dy="5">safety that lasts.</tspan></text>

    <text class="lobe-head" x="336" y="69">Relationships &amp; Bonds</text>
    <text class="lobe-sub" x="336" y="75">Close ties, steady growth</text>
    <text class="lobe-body"><tspan x="336" y="82">People who know us well</tspan><tspan x="336" dy="5">help us grow through</tspan><tspan x="336" dy="5">each stage of life.</tspan></text>

    <text class="lobe-head" x="410" y="115">Social Experiences</text>
    <text class="lobe-sub" x="410" y="121">Growing with others</text>
    <text class="lobe-body"><tspan x="410" y="128">Fun with friends lifts</tspan><tspan x="410" dy="5">mood and energy</tspan><tspan x="410" dy="5">across the week.</tspan></text>

    <circle cx="124" cy="104" r="2.5" fill="var(--gold)"/>
    <text class="lobe-head" x="130" y="106" style="fill:var(--gold)">Core Values</text>
    <text class="lobe-sub" x="130" y="112">What matters most</text>
    <text class="lobe-body"><tspan x="130" y="119">guides daily choices</tspan><tspan x="130" dy="5">and goals.</tspan></text>

    <text class="lobe-head" x="62" y="190">Embodiment</text>
    <text class="lobe-sub" x="62" y="196">Body and feeling</text>
    <text class="lobe-body"><tspan x="62" y="203">Rest, move, breathe</tspan><tspan x="62" dy="5">and notice.</tspan></text>

    <text class="lobe-head" x="62" y="224">Emotional State</text>
    <text class="lobe-sub" x="62" y="230">Calm mind, clear view</text>
    <text class="lobe-body"><tspan x="62" y="237">Notice the shifts</tspan><tspan x="62" dy="5">in mood.</tspan></text>

    <text class="lobe-head" x="62" y="318">Experiences</text>
    <text class="lobe-sub" x="62" y="324">New Growing Paths</text>
    <text class="lobe-body"><tspan x="62" y="331">Try, learn, and</tspan><tspan x="62" dy="5">reflect often.</tspan></text>
    <g role="img" aria-label="Two people walking together among falling leaves"><rect x="62" y="345" width="52" height="42" rx="10" fill="#e7b46a" opacity=".55"/></g>

    <text class="lobe-head" x="119" y="425">Joyful Experiences</text>
    <text class="lobe-sub" x="119" y="431">Shared Fun Brings Growth</text>
    <text class="lobe-body"><tspan x="119" y="438">Play and laughter</tspan><tspan x="119" dy="5">with loved ones</tspan><tspan x="119" dy="5">renew us.</tspan></text>

    <text class="lobe-head" x="197" y="468">Personal Growth</text>
    <text class="lobe-sub" x="197" y="474">Small steps each day</text>
    <circle cx="198" cy="480" r="2.5" fill="var(--red)"/>
    <text class="lobe-body"><tspan x="203" y="481">Learning from both</tspan><tspan x="203" dy="5">highs and lows</tspan><tspan x="203" dy="5">builds resilience.</tspan></text>

    <text class="lobe-head" x="343" y="468">Good Connections</text>
    <line x1="345" y1="477" x2="345" y2="498" stroke="var(--crimson)" stroke-width="2"/><circle cx="345" cy="476" r="3" fill="var(--crimson)"/>
    <text class="lobe-body"><tspan x="350" y="476">Kind words and</tspan><tspan x="350" dy="5">open listening</tspan><tspan x="350" dy="5">deepen each bond.</tspan></text>

    <text class="lobe-head" x="416" y="420">Healthy Habits</text>
    <text class="lobe-sub" x="416" y="426">Daily Care Routines</text>
    <text class="lobe-body"><tspan x="416" y="433">Sleep, food, and</tspan><tspan x="416" dy="5">time outside.</tspan></text>

    <text class="lobe-sub"><tspan x="459" y="208">Connected experiences</tspan><tspan x="459" dy="5">are better together</tspan></text>
    <text class="lobe-body" x="459" y="219">Sharing joy doubles it</text>

    <text class="lobe-head" x="481" y="320">Family Ties</text>
    <text class="lobe-body"><tspan x="481" y="328">Home is where we</tspan><tspan x="481" dy="5">first learn to trust.</tspan></text>

    <g role="img" aria-label="Two friends walking side by side"><rect x="458" y="148" width="50" height="46" rx="10" fill="#e9a24a" opacity=".5"/></g>
    <g role="img" aria-label="Person offering flowers to a friend"><rect x="500" y="250" width="44" height="48" rx="10" fill="#d9776a" opacity=".45"/></g>
    <g role="img" aria-label="Group of friends sitting together talking"><rect x="466" y="342" width="58" height="44" rx="10" fill="#4a84b8" opacity=".45"/></g>

    <text class="note"><tspan x="14" y="517">This map shows how relationships and experiences</tspan><tspan x="14" dy="5.5">work together to shape our wellbeing. When</tspan><tspan x="14" dy="5.5">we share positive moments with people we</tspan><tspan x="14" dy="5.5">trust, we thrive. Poor relationships and</tspan><tspan x="14" dy="5.5">negative experiences can hold us back.</tspan><tspan x="14" dy="5.5">Use each section to reflect on where</tspan><tspan x="14" dy="5.5">you are today and where you want</tspan><tspan x="14" dy="5.5">to grow next.</tspan></text>
    <text class="note" text-anchor="middle"><tspan x="500" y="534">Five key factors shape the journey:</tspan><tspan x="500" dy="5.5">relationships, experiences, mental state,</tspan><tspan x="500" dy="5.5">embodiment, and growth. Explore each</tspan><tspan x="500" dy="5.5">one with your therapist and notice</tspan><tspan x="500" dy="5.5">how they connect.</tspan><tspan x="500" dy="5.5">Adaptive-Harmonic Theory</tspan></text>
  </svg>

  <h1 class="title title-left">Lantern &amp;<br>Tides</h1>
  <h2 class="title title-right">Garden<br><span>of </span><span class="accent">Seasons</span></h2>
</main>
</body>
</html>
```